Estate Agent Board Design

Most eye-catching, elegant estate agent board
Company logo should stand out
Keyvault & CPRT should be small but visible.

On the board must be:

"FOR SALE"
logos
website hkwestates.co.uk
tel number 01632 960418

It Company

```html
<!DOCTYPE html>
<html lang="en">
<head>
<meta charset="utf-8">
<title>HKW Estates – For Sale Board</title>
<link rel="stylesheet" href="https://fonts.googleapis.com/css2?family=Arimo:wght@400;700&display=swap">
<style>
  :root {
    --board-grey: #d3d3d3;
    --band-light: #e2e2e2;
    --band-mid: #dadada;
    --brand-dark: #13260f;
    --brand-green: #1a6b0f;
    --panel-dark: #123210;
    --panel-green: #16800f;
    --lime-top: #52e60a;
    --lime-bottom: #2a7a14;
    --ink: #111111;
    --white: #ffffff;
    --seal-grey: #c9cfd6;
  }
  html, body {
    margin: 0;
    padding: 0;
    overflow: hidden;
    background: var(--board-grey);
  }
  .board {
    position: relative;
    width: 900px;
    height: 1200px;
    overflow: hidden;
    background: var(--board-grey);
    font-family: "Arimo", Arial, sans-serif;
  }
  .board-art {
    position: absolute;
    inset: 0;
  }
  .website {
    position: absolute;
    top: 12px;
    left: 0;
    width: 900px;
    text-align: center;
    font-size: 35px;
    color: var(--brand-dark);
    letter-spacing: 0.5px;
  }
  .brand {
    position: absolute;
    left: 35px;
    top: 110px;
    display: flex;
    align-items: center;
    gap: 22px;
  }
  .brand-dot {
    width: 70px;
    height: 70px;
    border-radius: 50%;
    background: var(--brand-green);
    flex: none;
  }
  .brand-name {
    font-size: 92px;
    font-weight: 700;
    line-height: 1;
    color: var(--brand-dark);
    white-space: nowrap;
  }
  .brand-tagline {
    position: absolute;
    left: 127px;
    top: 232px;
    font-size: 31px;
    font-weight: 700;
    color: var(--brand-dark);
    letter-spacing: 0.5px;
  }
  .headline {
    position: absolute;
    right: 12px;
    top: 470px;
    margin: 0;
    text-align: right;
    color: var(--white);
    font-weight: 400;
    line-height: 0.9;
  }
  .headline .for { font-size: 104px; display: block; }
  .headline .sale { font-size: 124px; display: block; }
  .partner-badge,
  .brand-badge {
    position: absolute;
    top: 1025px;
    height: 100px;
    background: var(--white);
  }
  .partner-badge { left: 43px; width: 105px; }
  .partner-badge .seal {
    position: absolute;
    left: 8px; top: 5px;
    width: 90px; height: 90px;
    border-radius: 50%;
    background: var(--seal-grey);
  }
  .brand-badge { left: 163px; width: 142px; }
  .brand-badge .mini-name {
    position: absolute;
    left: 0; top: 30px;
    width: 142px;
    text-align: center;
    font-size: 21px;
    font-weight: 700;
    line-height: 1;
    color: var(--brand-dark);
  }
  .brand-badge .mini-tagline {
    position: absolute;
    left: 0; top: 60px;
    width: 142px;
    text-align: center;
    font-size: 10px;
    font-weight: 700;
    color: var(--brand-dark);
  }
</style>
</head>
<body>
<main class="board">
  <svg class="board-art" width="900" height="1200" viewBox="0 0 900 1200" aria-hidden="true">
    <defs>
      <linearGradient id="panel-fade" x1="0" y1="0" x2="1" y2="0">
        <stop offset="0" stop-color="var(--panel-dark)"/>
        <stop offset="1" stop-color="var(--panel-green)"/>
      </linearGradient>
      <linearGradient id="corner-fade" x1="0" y1="0" x2="0" y2="1">
        <stop offset="0" stop-color="var(--lime-top)"/>
        <stop offset="1" stop-color="var(--lime-bottom)"/>
      </linearGradient>
    </defs>
    <g class="chevron-bands" fill="none" stroke-linejoin="miter">
      <polyline points="820,40 140,600 860,1230" stroke="var(--band-light)" stroke-width="60"/>
      <polyline points="880,40 230,600 900,1180" stroke="var(--band-mid)" stroke-width="50"/>
      <polyline points="900,120 330,600 900,1100" stroke="var(--band-light)" stroke-width="40"/>
    </g>
    <polygon class="sale-panel" points="900,140 430,575 900,990" fill="url(#panel-fade)"/>
    <polygon class="corner-panel" points="0,945 170,775 525,1138 462,1200 0,1200" fill="url(#corner-fade)"/>
    <text class="phone" x="190" y="790" transform="rotate(45 190 790)"
          font-family="Arimo, Arial, sans-serif" font-weight="700" font-size="72"
          fill="var(--ink)" letter-spacing="1">01632 960418</text>
  </svg>

  <div class="website">www.hkwestates.co.uk</div>

  <div class="brand">
    <div class="brand-dot"></div>
    <div class="brand-name">HKW Estates</div>
  </div>
  <div class="brand-tagline">SALES &amp; LETTINGS</div>

  <h1 class="headline">
    <span class="for">FOR</span>
    <span class="sale">SALE</span>
  </h1>

  <div class="partner-badge" aria-label="CPRT licensed member badge"><div class="seal"></div></div>
  <div class="brand-badge">
    <div class="mini-name">HKW Estates</div>
    <div class="mini-tagline">SALES &amp; LETTINGS</div>
  </div>
</main>
</body>
</html>
```